PELDRAX Business Cards

We require a business card for our company that provides IT consulting services. We already have a logo that needs to be used on the card. We want a clean professional looking design that incorporates our colours. Our main focus is providing managed services to business, which involves us looking after all of their IT requirements including managing servers/networks, projects, and procurement.

Industry/Entity Type

Information Technology

Requirements
Must have
• our logo, contact information, name, title, phone numbers

```html
<!DOCTYPE html>
<html lang="en">
<head>
<meta charset="utf-8">
<title>PELDRAX Business Cards</title>
<link rel="stylesheet" href="https://fonts.googleapis.com/css2?family=Montserrat:wght@400;500;600&display=swap">
<style>
  :root {
    --stage: #3b3b3d;
    --paper: #ffffff;
    --ink-dark: #1d1e21;
    --brand-blue: #1a94d3;
    --text-grey: #555a60;
    --text-light: #e6e8ea;
  }
  * { box-sizing: border-box; margin: 0; padding: 0; }
  html, body { width: 1200px; height: 900px; overflow: hidden; }
  body {
    background: var(--stage);
    font-family: "Montserrat", sans-serif;
    position: relative;
  }
  .card { position: absolute; overflow: hidden; }
  .card--landscape { width: 514px; height: 297px; background: var(--paper); top: 30px; }
  .card--portrait { width: 298px; height: 514px; background: var(--ink-dark); top: 355px; }
  .front-light { left: 73px; }
  .back-light { left: 615px; }
  .front-dark { left: 289px; }
  .back-dark { left: 615px; }

  .wordmark {
    position: absolute;
    display: flex; align-items: center; gap: 10px;
    color: var(--brand-blue);
    font-weight: 500;
    letter-spacing: 2px;
  }
  .wordmark__dot { background: var(--brand-blue); border-radius: 50%; flex: none; }

  .front-light .wordmark { left: 0; right: 0; justify-content: center; top: 118px; font-size: 40px; }
  .front-light .wordmark__dot { width: 40px; height: 40px; }
  .front-light .web { position: absolute; left: 0; right: 0; bottom: 30px; text-align: center; font-size: 13px; color: var(--text-grey); }
  .web b { color: var(--brand-blue); font-weight: 500; }

  .back-light .wordmark { left: 48px; top: 50px; font-size: 38px; }
  .back-light .wordmark__dot { width: 40px; height: 40px; }
  .person { position: absolute; text-align: right; }
  .person__name { color: var(--brand-blue); font-weight: 500; }
  .person__title { font-size: 10px; color: var(--text-grey); letter-spacing: .3px; }
  .back-light .person { right: 30px; top: 144px; }
  .back-light .person__name { font-size: 17px; }
  .address { position: absolute; font-size: 12.5px; line-height: 16px; color: var(--text-grey); }
  .back-light .address { left: 48px; top: 186px; }
  .contacts { position: absolute; text-align: right; font-size: 12.5px; line-height: 17px; color: var(--text-grey); list-style: none; }
  .contacts li { display: flex; justify-content: flex-end; align-items: center; gap: 6px; }
  .contacts svg { width: 11px; height: 11px; flex: none; }
  .back-light .contacts { right: 30px; top: 201px; }
  .band { position: absolute; left: 0; right: 0; bottom: 0; height: 33px; background: var(--brand-blue); display: flex; align-items: center; gap: 9px; padding-left: 48px; }
  .band span { width: 11px; height: 11px; background: var(--paper); border-radius: 2px; }

  .front-dark .wordmark { left: 0; right: 0; justify-content: center; top: 235px; font-size: 30px; flex-direction: column; gap: 24px; }
  .front-dark .wordmark__dot { width: 120px; height: 120px; }

  .back-dark .person { right: 26px; top: 44px; }
  .back-dark .person__name { font-size: 21px; line-height: 24px; font-weight: 400; }
  .back-dark .person__title { color: var(--text-light); font-size: 11px; }
  .back-dark .contacts { right: 26px; top: 136px; color: var(--text-light); font-size: 13px; }
  .decor { position: absolute; left: 0; top: 190px; width: 200px; height: 324px; background: linear-gradient(160deg, #1a94d3, #0f7fbd); clip-path: polygon(0 0, 100% 22%, 0 100%); }
  .back-dark .address { right: 26px; top: 365px; text-align: right; color: var(--text-light); font-size: 13px; line-height: 17px; }
  .back-dark .web { position: absolute; right: 26px; bottom: 40px; font-size: 13px; color: var(--text-light); }
</style>
</head>
<body>
  <section class="card card--landscape front-light">
    <div class="wordmark"><span class="wordmark__dot"></span>PELDRAX</div>
    <p class="web">www.<b>peldrax</b>.com</p>
  </section>

  <section class="card card--landscape back-light">
    <div class="wordmark"><span class="wordmark__dot"></span>PELDRAX</div>
    <div class="person">
      <p class="person__name">DORIAN HALVECKS</p>
      <p class="person__title">MANAGING DIRECTOR</p>
    </div>
    <p class="address">47 Ridgeline Road<br>PO Box 2264<br>Marlow Creek, AB<br>T0K 3B1</p>
    <ul class="contacts">
      <li>555 240 7781 <svg viewBox="0 0 12 12"><rect x=".5" y=".5" width="11" height="11" rx="2" fill="none" stroke="#1a94d3"/><path d="M3.5 4c0 2.5 2 4.5 4.5 4.5" fill="none" stroke="#1a94d3" stroke-width="1.4" stroke-linecap="round"/></svg></li>
      <li>888 316 4402 <svg viewBox="0 0 12 12"><rect x=".5" y=".5" width="11" height="11" rx="2" fill="none" stroke="#1a94d3"/><rect x="4" y="2.8" width="4" height="6.4" rx="1" fill="none" stroke="#1a94d3"/></svg></li>
      <li>d.halvecks@peldrax.com <svg viewBox="0 0 12 12"><rect x=".5" y=".5" width="11" height="11" rx="2" fill="#1a94d3"/><path d="M3 4.5l3 2 3-2" fill="none" stroke="#fff"/></svg></li>
    </ul>
    <div class="band"><span></span><span></span><span></span><span></span><span></span></div>
  </section>

  <section class="card card--portrait front-dark">
    <div class="wordmark"><span class="wordmark__dot"></span>PELDRAX</div>
  </section>

  <section class="card card--portrait back-dark">
    <div class="person">
      <p class="person__name">DORIAN<br>HALVECKS</p>
      <p class="person__title">MANAGING DIRECTOR</p>
    </div>
    <ul class="contacts">
      <li>555 240 7781 <svg viewBox="0 0 12 12"><rect x=".5" y=".5" width="11" height="11" rx="2" fill="none" stroke="#1a94d3"/><path d="M3.5 4c0 2.5 2 4.5 4.5 4.5" fill="none" stroke="#1a94d3" stroke-width="1.4" stroke-linecap="round"/></svg></li>
      <li>888 316 4402 <svg viewBox="0 0 12 12"><rect x=".5" y=".5" width="11" height="11" rx="2" fill="none" stroke="#1a94d3"/><rect x="4" y="2.8" width="4" height="6.4" rx="1" fill="none" stroke="#1a94d3"/></svg></li>
      <li>d.halvecks@peldrax.com <svg viewBox="0 0 12 12"><rect x=".5" y=".5" width="11" height="11" rx="2" fill="#1a94d3"/><path d="M3 4.5l3 2 3-2" fill="none" stroke="#fff"/></svg></li>
    </ul>
    <div class="decor" role="img" aria-label="Large blue brand emblem decoration"></div>
    <p class="address">47 Ridgeline Road<br>PO Box 2264<br>Marlow Creek, AB<br>T0K 3B1</p>
    <p class="web">www.<b>peldrax</b>.com</p>
  </section>
</body>
</html>
```